Brightwell Recovery Email Marketing Design

Dear Designer,
We're in need of an email background template for our company, Brightwell Recovery, that reflects our commitment to building lasting relationships with our clients and providing top-quality restoration and cleaning services.
We'd like the template to incorporate our brand colors, which are #F2F2F3, #005EA5, #468ECC, and #000000, and to feature images related to our services, such as water restoration, emergency flood response, mold remediation, trauma scene clean-up, fire restoration, carpet cleaning, and more. Our logo and tagline, "Calm Returns", should be prominently displayed in a unique and visually appealing way, along with our website address, www.brightwellrecovery.example.
The email should be professional and positive, highlighting the camaraderie and teamwork among our employees. We want to thank our clients for their business, offer a special discount, and promote our services. The final design should be visually stunning and memorable, with a clear call-to-action to encourage clients to take advantage of the discount.
We'd like the final design in JPG or PNG format, with a resolution of at least 720x720 pixels.
Thank you for considering this project. We're excited to see what you come up with!
Best regards,
Tavin

```html
<!DOCTYPE html>
<html lang="en">
<head>
<meta charset="utf-8">
<title>Brightwell Recovery – Calm Returns</title>
<link rel="stylesheet" href="https://fonts.googleapis.com/css2?family=Montserrat:wght@600;700;800&family=Nunito+Sans:wght@400;600&display=swap">
<style>
  :root {
    --brand-deep: #005EA5;
    --brand-sky: #468ECC;
    --brand-mist: #F2F2F3;
    --brand-ink: #000000;
    --heading-tint: #9FCBF0;
    --white: #FFFFFF;
  }
  * { margin: 0; padding: 0; box-sizing: border-box; }
  html, body { width: 1200px; height: 1200px; overflow: hidden; background: var(--brand-deep); }
  .email {
    position: relative;
    width: 1200px;
    height: 1200px;
    background: var(--brand-deep);
    color: var(--white);
    font-family: "Nunito Sans", Arial, sans-serif;
  }
  .hero {
    position: absolute; left: 0; top: 0; width: 1200px; height: 213px;
    background: radial-gradient(ellipse at 50% 40%, #3a3d42 0%, #16181b 55%, var(--brand-ink) 100%);
  }
  .brand {
    position: absolute; left: 0; top: 0; width: 1200px; height: 213px;
    display: flex; align-items: center; justify-content: center; gap: 22px;
  }
  .brand-mark {
    width: 30px; height: 30px; border-radius: 50%; background: var(--brand-sky);
  }
  .brand-name {
    font-family: "Montserrat", Arial, sans-serif; font-weight: 800;
    font-size: 64px; letter-spacing: 2px; text-transform: uppercase; color: var(--white);
  }
  .tagline-band {
    position: absolute; left: 0; top: 213px; width: 1200px; height: 100px;
    background: var(--brand-sky);
    display: flex; align-items: center; justify-content: center;
  }
  .tagline {
    font-family: "Montserrat", Arial, sans-serif; font-weight: 700;
    font-size: 46px; letter-spacing: 1px; text-transform: uppercase;
  }
  .services-title {
    position: absolute; left: 0; top: 358px; width: 1200px; text-align: center;
    font-family: "Montserrat", Arial, sans-serif; font-weight: 700;
    font-size: 34px; color: var(--heading-tint); text-transform: uppercase;
  }
  .service {
    position: absolute; width: 400px; margin-left: -200px; text-align: center;
  }
  .service-icon { display: block; width: 72px; height: 72px; margin: 0 auto 24px; }
  .service-label { font-size: 26px; font-weight: 400; }
  .clients-band {
    position: absolute; left: 0; top: 827px; width: 1200px; height: 100px;
    background: var(--brand-sky);
  }
  .clients-heading {
    position: absolute; left: 48px; top: 0; height: 100px; line-height: 100px;
    font-family: "Montserrat", Arial, sans-serif; font-weight: 700; font-size: 33px;
  }
  .client-name {
    position: absolute; top: 0; height: 100px; line-height: 100px;
    font-family: "Nunito Sans", Arial, sans-serif; font-weight: 600; font-size: 24px;
    transform: translateX(-50%); white-space: nowrap; color: var(--brand-mist);
  }
  .offer {
    position: absolute; left: 48px; top: 965px; width: 670px; text-align: center;
    font-family: "Montserrat", Arial, sans-serif; font-weight: 700; font-size: 46px;
    text-transform: uppercase; line-height: 72px;
  }
  .offer-highlight {
    display: inline-block; background: var(--brand-sky); padding: 0 16px; line-height: 64px;
  }
  .cta {
    position: absolute; left: 780px; top: 980px; width: 358px; height: 113px;
    background: var(--brand-sky);
    display: flex; align-items: center; justify-content: center;
    font-family: "Montserrat", Arial, sans-serif; font-weight: 700; font-size: 37px;
    text-transform: uppercase; color: var(--white); text-decoration: none;
  }
  .website {
    position: absolute; left: 0; top: 1133px; width: 1200px; text-align: center;
    font-size: 26px; color: var(--white);
  }
</style>
</head>
<body>
<main class="email">
  <div class="hero" role="img" aria-label="Dark backdrop of water droplets on black glass"></div>
  <div class="brand">
    <span class="brand-mark"></span>
    <span class="brand-name">Brightwell Recovery</span>
  </div>

  <div class="tagline-band"><h1 class="tagline">Calm Returns</h1></div>

  <h2 class="services-title">Our Services</h2>

  <div class="service" style="left:190px; top:450px;">
    <svg class="service-icon" viewBox="0 0 72 72" aria-hidden="true">
      <path d="M36 6 C36 6 14 32 14 46 a22 22 0 0 0 44 0 C58 32 36 6 36 6 Z" fill="#fff"/>
      <path d="M24 46 a12 12 0 0 0 10 12" stroke="#005EA5" stroke-width="4" fill="none" stroke-linecap="round"/>
    </svg>
    <p class="service-label">Water Restoration</p>
  </div>

  <div class="service" style="left:597px; top:450px;">
    <svg class="service-icon" viewBox="0 0 72 72" aria-hidden="true" fill="none" stroke="#fff" stroke-width="5" stroke-linejoin="round" stroke-linecap="round">
      <path d="M8 32 L36 8 L64 32"/>
      <path d="M16 28 V50 H56 V28"/>
      <path d="M30 50 V38 H42 V50"/>
      <path d="M6 60 q6 -5 12 0 t12 0 t12 0 t12 0 t12 0"/>
    </svg>
    <p class="service-label">Emergency flood response</p>
  </div>

  <div class="service" style="left:1012px; top:450px;">
    <svg class="service-icon" viewBox="0 0 72 72" aria-hidden="true" fill="#fff">
      <circle cx="20" cy="28" r="11"/><circle cx="50" cy="16" r="12"/>
      <circle cx="44" cy="52" r="13"/><circle cx="14" cy="58" r="5"/>
      <circle cx="32" cy="8" r="3"/><circle cx="66" cy="38" r="3"/><circle cx="6" cy="14" r="3"/>
      <g fill="#005EA5"><circle cx="18" cy="26" r="2"/><circle cx="48" cy="14" r="2.5"/><circle cx="54" cy="20" r="1.5"/><circle cx="40" cy="50" r="2.5"/><circle cx="48" cy="56" r="2"/></g>
    </svg>
    <p class="service-label">Mould Remediation</p>
  </div>

  <div class="service" style="left:190px; top:645px;">
    <svg class="service-icon" viewBox="0 0 72 72" aria-hidden="true" fill="none" stroke="#fff" stroke-width="4.5" stroke-linecap="round" stroke-linejoin="round">
      <rect x="30" y="20" width="26" height="20" rx="4" transform="rotate(-40 43 30)"/>
      <path d="M12 52 L30 34 M20 60 L38 42"/>
      <path d="M8 10 l6 6 M18 6 l2 8 M6 22 l8 0"/>
      <path d="M46 56 l6 6 M56 50 l8 2 M44 66 l2 4"/>
    </svg>
    <p class="service-label">Trauma scene clean-up</p>
  </div>

  <div class="service" style="left:597px; top:645px;">
    <svg class="service-icon" viewBox="0 0 72 72" aria-hidden="true" fill="#fff">
      <path d="M6 66 C2 48 12 40 14 28 C20 38 18 46 22 52 C24 40 30 32 30 18 C40 30 38 42 40 50 C44 42 44 34 50 26 C56 40 52 48 56 54 C60 48 60 40 66 36 C70 48 70 58 66 66 Z"/>
    </svg>
    <p class="service-label">Fire Restoration</p>
  </div>

  <div class="service" style="left:1012px; top:645px;">
    <svg class="service-icon" viewBox="0 0 72 72" aria-hidden="true">
      <rect x="6" y="20" width="30" height="38" rx="3" fill="none" stroke="#fff" stroke-width="4.5"/>
      <path d="M12 30 H30 M12 40 H30 M12 50 H30" stroke="#fff" stroke-width="3"/>
      <rect x="34" y="10" width="32" height="26" rx="8" fill="#fff"/>
      <g fill="#005EA5"><circle cx="44" cy="20" r="2.5"/><circle cx="54" cy="26" r="2.5"/><circle cx="58" cy="17" r="2"/></g>
      <path d="M40 46 q6 -4 12 0 t12 0" stroke="#fff" stroke-width="4" fill="none" stroke-linecap="round"/>
    </svg>
    <p class="service-label">Carpet Cleaning</p>
  </div>

  <section class="clients-band">
    <h3 class="clients-heading">We thank our clients</h3>
    <span class="client-name" style="left:508px;">HARBOR &amp; VINE</span>
    <span class="client-name" style="left:697px;">Pawline</span>
    <span class="client-name" style="left:917px;">Fernfield</span>
    <span class="client-name" style="left:1120px;">Oakmere</span>
  </section>

  <p class="offer">Special Discount Offer<br>With <span class="offer-highlight">50% Offer</span></p>
  <a class="cta" href="#">Book Now</a>

  <p class="website">www.brightwellrecovery.example</p>
</main>
</body>
</html>
```